Signboard menu for a Fastfood takeaway shop

My current signboard menu is old now, I want to upgrade to a new, bigger and brighter signboard menu.
Photos of the old menu attached but there are some changes in each sections of the menu needs to be changed.
Size of the signboard :
L: 1700cm
H: 1200cm

Industry/Entity Type

Fastfood Hospitality

Colors
FFC000
F8CF3A
FAE287
FDF2CF
FEFAEE

```html
<!DOCTYPE html>
<html lang="en">
<head>
<meta charset="utf-8">
<title>Takeaway Menu Board</title>
<link rel="stylesheet" href="https://fonts.googleapis.com/css2?family=Arimo:wght@400;700&family=Great+Vibes&display=swap">
<style>
:root{
  --backdrop:#c6c7c6;
  --panel-top:#f27d5a;
  --panel-bottom:#f36525;
  --ink:#111111;
  --light:#ffffff;
  --rule:rgba(255,255,255,0.85);
}
*{margin:0;padding:0;box-sizing:border-box}
html,body{width:1200px;height:912px;overflow:hidden;background:var(--backdrop)}
.board{position:relative;width:1200px;height:912px;font-family:"Arimo",Arial,sans-serif;color:var(--light)}
.band{position:absolute;left:76px;width:1048px}
.band-top{top:86px;height:524px;background:var(--panel-top)}
.band-bottom{top:610px;height:216px;background:var(--panel-bottom)}
.title{position:absolute;left:0;width:1200px;top:90px;text-align:center;font-family:"Great Vibes",cursive;font-size:92px;line-height:1;color:var(--light)}
.head,.col{position:absolute;border:1px dashed var(--rule)}
.head{height:25px;padding-left:9px;font-weight:700;font-size:14.5px;line-height:23px;color:var(--ink);letter-spacing:.3px}
.head small{font-size:7px;letter-spacing:0}
.col{--l:9px;--r:4px}
.item{position:absolute;left:var(--l);right:var(--r);display:flex;justify-content:space-between;align-items:flex-start;font-size:11px;line-height:13px}
.item .low{align-self:flex-end}
.item sub,.note{font-size:7.5px;color:var(--ink);vertical-align:baseline}
.note{position:absolute;left:var(--l);font-weight:700;line-height:10px}
.tag{font-size:8px;color:var(--ink)}
</style>
</head>
<body>
<div class="board">
  <div class="band band-top"></div>
  <div class="band band-bottom"></div>
  <h1 class="title">Menu</h1>

  <!-- Sandwiches -->
  <div class="head" style="left:99px;top:179px;width:324px">SANDWICHES</div>
  <div class="col" style="left:99px;top:207px;width:158px;height:188px;--r:3px">
    <div class="item" style="top:2px"><span>Baked Beans</span><span>$4.50</span></div>
    <div class="item" style="top:23px"><span>Yeast Spread</span><span>$3.60</span></div>
    <div class="item" style="top:44px"><span>Cheese</span><span>$3.50</span></div>
    <div class="item" style="top:66px"><span>Tomato</span><span>$3.50</span></div>
    <div class="item" style="top:89px"><span>Salad</span><span>$6.00</span></div>
    <div class="item" style="top:111px"><span>Ham</span><span>$6.50</span></div>
    <div class="item" style="top:132px"><span>Chicken</span><span>$6.50</span></div>
    <div class="item" style="top:153px"><span>Roast Beef</span><span>$6.50</span></div>
    <div class="item" style="top:170px"><span>Tuna</span><span>$6.50</span></div>
  </div>
  <div class="col" style="left:263px;top:207px;width:160px;height:188px;--l:5px;--r:10px">
    <div class="item" style="top:2px"><span>Rissole</span><span>$6.60</span></div>
    <div class="item" style="top:23px"><span>Sausage</span><span>$6.00</span></div>
    <div class="item" style="top:45px"><span>Scallop</span><span>$5.00</span></div>
    <div class="item" style="top:67px"><span>Chip</span><span>$5.00</span></div>
    <div class="item" style="top:89px"><span>Bacon</span><span>$6.00</span></div>
    <div class="item" style="top:111px"><span>Bacon/Egg</span><span>$6.00</span></div>
    <div class="item" style="top:132px"><span>Schnitzel</span><span>$7.50</span></div>
    <div class="item" style="top:153px"><span>Roll</span><span>+50d</span></div>
    <div class="item" style="top:171px"><span class="tag"><b>CREATE YOUR OWN FOR</b></span><span>$</span></div>
  </div>

  <!-- Burgers -->
  <div class="head" style="left:438px;top:179px;width:322px;padding-left:10px">BURGERS <small>(BEEF OR CHICKEN)</small></div>
  <div class="col" style="left:438px;top:207px;width:160px;height:188px;--l:10px;--r:4px">
    <div class="item" style="top:2px"><span>Plain</span><span>$7.00</span></div>
    <div class="item" style="top:23px"><span>Works</span><span>$8.00</span></div>
    <div class="item" style="top:46px"><span>Cheese</span><span>$7.50</span></div>
    <div class="item" style="top:67px"><span>Egg</span><span>$8.00</span></div>
    <div class="item" style="top:89px"><span>Pineapple</span><span>$7.50</span></div>
    <div class="item" style="top:110px"><span>Vegie</span><span>$7.50</span></div>
    <div class="item" style="top:131px"><span>Hawaiion</span><span>$9.00</span></div>
    <div class="item" style="top:153px"><span>Fish</span><span>$7.50</span></div>
    <div class="item" style="top:172px"><span>Bacon</span><span>$8.00</span></div>
  </div>
  <div class="col" style="left:603px;top:207px;width:157px;height:188px;--l:2px;--r:10px">
    <div class="item" style="top:2px"><span>Bacon/Egg</span><span>$8.00</span></div>
    <div class="item" style="top:23px"><span>Bacon/Cheese</span><span>$8.00</span></div>
    <div class="item" style="top:45px"><span>Mexican</span><span>$7.50</span></div>
    <div class="item" style="top:67px"><span>Mega</span><span>$14.00</span></div>
    <div class="note" style="top:82px">(Double Works)</div>
  </div>

  <!-- Hot food -->
  <div class="head" style="left:779px;top:179px;width:322px;padding-left:11px">HOT FOOD</div>
  <div class="col" style="left:779px;top:207px;width:160px;height:188px;--l:11px;--r:3px">
    <div class="item" style="top:2px"><span>Scallop</span><span>$2.00</span></div>
    <div class="item" style="top:23px"><span>Dim Sim</span><span>$2.00</span></div>
    <div class="item" style="top:44px"><span>Hash Brown</span><span>$2.50</span></div>
    <div class="item" style="top:66px"><span>Sausage</span><span>$3.00</span></div>
    <div class="item" style="top:90px"><span>Corn Jack</span><span>$3.50</span></div>
    <div class="item" style="top:111px"><span>Rissole</span><span>$4.00</span></div>
    <div class="item" style="top:132px"><span>Chicken Stick</span><span>$3.70</span></div>
    <div class="item" style="top:153px"><span>Veggie Roll</span><span>$3.50</span></div>
    <div class="item" style="top:170px"><span>Spring Roll</span><span>$3.50</span></div>
  </div>
  <div class="col" style="left:945px;top:207px;width:156px;height:188px;--l:3px;--r:6px">
    <div class="item" style="top:2px"><b>Battered Sav</b><span>$3.60</span></div>
    <div class="item" style="top:24px"><b>Battered Pup</b><span>$4.50</span></div>
    <div class="item" style="top:46px"><b>Mini Chicken<br>Dim Sim *6</b><span>$3.00</span></div>
    <div class="item" style="top:90px"><b>Chicken Dim Sim</b><span>$5.00</span></div>
    <div class="item" style="top:111px"><b>Chips <small style="font-size:8px">From</small></b><span>$4.00</span></div>
    <div class="item" style="top:133px"><b>Chips &amp; Gravy</b><span>$5.50</span></div>
  </div>

  <!-- Seafood packs -->
  <div class="head" style="left:99px;top:402px;width:324px">SEAFOOD PACKS</div>
  <div class="col" style="left:99px;top:430px;width:324px;height:170px;--l:9px;--r:9px">
    <div class="item" style="top:7px"><span>1Leg Fish &amp; Chips</span><span>$8.00</span></div>
    <div class="item" style="top:29px"><span>2 Calamari, 2 Prawn Cutlet &amp; Chips</span><span>$7.00</span></div>
    <div class="item" style="top:50px"><span>1 Calamari, 1 Prawn Cutlet, 1 Seafood Stick</span><span>$8.50</span></div>
    <div class="item" style="top:72px"><span>3 Cocktail Fish &amp; Chips</span><span>$8.00</span></div>
    <div class="item" style="top:94px"><span>1 Cocktail Fish, 1 Crab Stick, 2 Prawn Cutlets,<br>2 Calamari Ring &amp; Chips</span><span>$12.50</span></div>
    <div class="item" style="top:134px"><span>Family... 4 Prawn Cutlets, 6 Cocktail Fish,<br>4 Calamari Rings, $4 Chips &amp; 1.25L Drink</span><span>$34.00</span></div>
  </div>

  <!-- Salads -->
  <div class="head" style="left:438px;top:402px;width:160px;padding-left:10px">SALADS IN TUBS</div>
  <div class="col" style="left:438px;top:430px;width:160px;height:170px;--l:10px;--r:4px">
    <div class="item" style="top:2px"><span>Caesar</span><span>$8.00</span></div>
    <div class="item" style="top:23px"><span>Extras<sub>(Pineapple)</sub></span><span>$0.70</span></div>
    <div class="item" style="top:44px"><span>Avocado<sub>(Sauce)</sub></span><span><sub>50C</sub>&nbsp;&nbsp;$1.20</span></div>
    <div class="item" style="top:67px"><span>Cheese</span><span>$1.00</span></div>
    <div class="item" style="top:89px"><span>Bacon/Meat</span><span>$2.50</span></div>
    <div class="item" style="top:111px"><span>Egg</span><span>$1.50</span></div>
    <div class="item" style="top:133px"><span>Kebab Meat<sub>(beef)</sub></span><span>$3.50</span></div>
    <div class="item" style="top:152px"><span>Chicken<sub>(100g)</sub></span><span>$4.00</span></div>
  </div>

  <!-- Seafood -->
  <div class="head" style="left:603px;top:402px;width:157px;padding-left:2px">SEAFOOD</div>
  <div class="col" style="left:603px;top:430px;width:157px;height:170px;--l:2px;--r:9px">
    <div class="item" style="top:2px"><span>Calamari Rings</span><span>$1.50</span></div>
    <div class="item" style="top:22px"><span>Cocktail Fish</span><span>$2.50</span></div>
    <div class="item" style="top:43px"><span>Crab Stick</span><span>$2.50</span></div>
    <div class="item" style="top:63px"><span>Prawn Cutlet</span><span>$2.30</span></div>
    <div class="item" style="top:85px"><span>Fish Cake</span><span>$</span></div>
    <div class="item" style="top:105px"><span>Battered Fish</span><span>$6.50</span></div>
    <div class="item" style="top:128px"><span>Crumbed Fish</span><span>$</span></div>
  </div>

  <!-- Big brekky -->
  <div class="head" style="left:779px;top:402px;width:322px;padding-left:11px">BIG BREKKY</div>
  <div class="col" style="left:779px;top:430px;width:322px;height:170px;--l:11px;--r:11px">
    <div class="item" style="top:1px"><span>Bacon, *2 Eggs, Sausage, Fried Tomato,<br>Hash Brown &amp; *2 Slices Toast</span><span>$13.00</span></div>
    <div class="item" style="top:35px"><span>Bacon, *2 Eggs, Sausage, Fried Tomato,<br>Hash Brown &amp; *2 Slices Toast (with coffee)</span><span class="low">$0.70</span></div>
    <div class="item" style="top:68px"><span>Snack Packs <sub>SML</sub></span></div>
    <div class="item" style="top:90px"><span>Chicken Mixed <sub>LEG</sub></span></div>
    <div class="item" style="top:96px"><span></span><span>$14.50</span></div>
    <div class="note" style="top:113px">SAUCE OF YOUR CHOICE</div>
    <div class="item" style="top:114px"><span></span><span>$19.50</span></div>
  </div>

  <!-- Schnitzel wraps -->
  <div class="head" style="left:99px;top:625px;width:158px;height:24px">SCHNITZEL WRAPS</div>
  <div class="col" style="left:99px;top:652px;width:158px;height:154px;--l:9px;--r:3px">
    <div class="item" style="top:2px"><span>Schnitzel Caesar</span><span>$11.00</span></div>
    <div class="item" style="top:23px"><span>Schnitzel, Salad<br>&amp; Cheese</span><span>$9.50</span></div>
    <div class="item" style="top:58px"><span>Schnitzel, Chips<br>&amp; Garlic Sauce</span><span>$6.50</span></div>
    <div class="item" style="top:92px"><span>Schnitzel Works</span><span>$11.50</span></div>
    <div class="note" style="top:103px;font-weight:400">(Bacon, Egg,<br>Cheese &amp; Salad)</div>
    <div class="item" style="top:129px"><span>Schnitzel Maxican</span><span>$9.50</span></div>
  </div>

  <!-- Gravy rolls -->
  <div class="head" style="left:263px;top:625px;width:160px;height:24px;padding-left:5px">GRAVY ROLLS</div>
  <div class="col" style="left:263px;top:652px;width:160px;height:154px;--l:5px;--r:9px">
    <div class="item" style="top:2px"><span>Roast Beef</span><span>$8.00</span></div>
    <div class="item" style="top:24px"><span>Chicken</span><span>$7.00</span></div>
    <div class="item" style="top:46px"><span>Rissole</span><span>$7.00</span></div>
    <div class="item" style="top:70px"><span>Sausage</span><span>$</span></div>
    <div class="item" style="top:91px"><span>Schnitzel</span><span>$7.50</span></div>
    <div class="item" style="top:112px"><span>Chip</span><span>$6.50</span></div>
  </div>

  <!-- Kebabs -->
  <div class="head" style="left:438px;top:625px;width:160px;height:24px;padding-left:10px">KEBABS</div>
  <div class="col" style="left:438px;top:652px;width:160px;height:154px;--l:10px;--r:4px">
    <div class="item" style="top:2px"><span>Lamb</span><span>$14.00</span></div>
    <div class="item" style="top:24px"><span>Mixed</span><span>$14.00</span></div>
    <div class="item" style="top:46px"><span>Chicken</span><span>$12.50</span></div>
  </div>

  <!-- Hot dogs -->
  <div class="head" style="left:603px;top:625px;width:157px;height:24px;padding-left:2px">HOT DOGS</div>
  <div class="col" style="left:603px;top:652px;width:157px;height:154px;--l:2px;--r:9px">
    <div class="item" style="top:4px"><span>Plain</span><span>$6.00</span></div>
    <div class="item" style="top:25px"><span>Cheese</span><span>$6.50</span></div>
    <div class="item" style="top:47px"><span>Cheese &amp; Bacon</span><span>$7.00</span></div>
    <div class="item" style="top:70px"><span>Double Hot Dog</span><span>$9.00</span></div>
    <div class="item" style="top:92px"><span>Works</span><span>$8.50</span></div>
    <div class="note" style="top:107px">OR CREATE YOUR OWN</div>
  </div>

  <!-- Bacon & egg rolls -->
  <div class="head" style="left:779px;top:625px;width:322px;height:24px;padding-left:11px">BANCON/EGG ROLLS</div>
  <div class="col" style="left:779px;top:652px;width:322px;height:154px;--l:11px;--r:16px">
    <div class="item" style="top:2px"><span>Bancon &amp; Egg</span><span>$7.00</span></div>
    <div class="item" style="top:22px"><span>Bacon, Egg &amp; Cheese</span><span>$7.50</span></div>
    <div class="item" style="top:47px"><span>Bacon, Egg, Cheese &amp; Onion</span><span>$7.50</span></div>
    <div class="item" style="top:70px"><span>Bacon, Egg, Cheese &amp; Avocado</span><span>$8.50</span></div>
  </div>
</div>
</body>
</html>
```